Design a logo and an adult website to upload our amateur mature milf videos filmed on Maui*

Aloha,

We need a website and a logo design for my adult website, we have a domain already. Marisolvelvet.com via Hostwrenly, We are based on the island of Maui, Hawaii. We'd like to feature the word "Filmed in Tropical Locations" instead of Maui though. We want to upload amateur solo girl videos and would like to have customers be able to be driven to our site to view short clips and then become members via a monthly membership. We'd also like to be able to have an area where we can post links to items that the customer can purchase that I can wear, use, etc. I'm new to all of this, so you'll have your work cut out for you. I'm open to more suggestions. The genre for my videos is amateur mature milf.

Thank you so much!

Payment is now guaranteed. I look forward to your submissions.

Target Market(s)

anyone interested in mature amateur milf videos

Industry/Entity Type

Adult

Coding

Coded - Design and coding required

Number of Pages Required

1 page

Font styles to use
Script

Requirements
Must have
• able to upload many videos; membership area; store area for customers to buy me toys, costumes and outfits to wear on camera; sneak peak area to view short clips for free. Area for still photos. Categories for videos: Outdoor videos; Naughty Costumes; Slutty Whore-Shoes;
Nice to have
• I like black and hot pink as colors, but I am very open to your ideas and designs. I'm a flashy, rhinestone and hot pink kinda girl, fyi. Let's keep it fun and sexy! :)

For the logo I would like pink kiss lips next to the lettering Marisol Velvet. I have uploaded a sample of what I designed. It says .com in it, but please remove that part. Thanks!
Should not have
• Please do not use Maui or Hawaii. I don't want people to know where I reside. Please use the words Exotic tropical locations, instead.

```html
<!DOCTYPE html>
<html lang="en">
<head>
<meta charset="utf-8">
<title>Marisol Velvet</title>
<link rel="stylesheet" href="https://fonts.googleapis.com/css2?family=IBM+Plex+Sans:ital,wght@0,400;0,500;0,600;1,400&family=Great+Vibes&display=swap">
<style>
  :root {
    --ink: #0f0c10;
    --panel: #1b1a1c;
    --panel-line: #3a2a30;
    --pink: #fb6ec0;
    --pink-soft: #ff77c6;
    --pink-deep: #e0329a;
    --red-badge: #e8103a;
    --white: #ffffff;
    --muted: #d9d4d8;
    --grey-card: #4a4a4c;
    --ring: #4b2d3d;
  }
  * { box-sizing: border-box; margin: 0; padding: 0; }
  html, body { width: 1200px; height: 3341px; overflow: hidden; background: var(--ink); }
  body { font-family: "IBM Plex Sans", Arial, sans-serif; color: var(--white); }
  .page { position: relative; width: 1200px; height: 3341px; overflow: hidden; background: var(--ink); }
  .abs { position: absolute; }

  /* header backdrop */
  .side-photo { top: 0; width: 200px; height: 720px;
    background: linear-gradient(180deg, #3b3b3d 0%, #1e1d1f 60%, var(--ink) 100%); }
  .side-photo.left { left: 0; }
  .side-photo.right { right: 0; }

  .brand { display: flex; align-items: center; gap: 12px; font-size: 30px; font-weight: 500; color: var(--pink); }
  .brand-dot { width: 34px; height: 34px; border-radius: 50%; background: var(--pink); }
  .site-header .brand { left: 144px; top: 28px; }
  .main-nav { left: 558px; top: 38px; display: flex; gap: 27px; font-size: 16px; }
  .main-nav a { color: var(--white); text-decoration: none; padding-bottom: 8px; }
  .main-nav a.active { border-bottom: 2px solid var(--pink); }
  .cart { left: 1012px; top: 32px; }

  /* hero */
  .hero { left: 144px; top: 105px; width: 912px; height: 606px;
    background: linear-gradient(180deg, #b796c4 0%, #d8a2a8 28%, #4b8aa8 50%, #7a4a52 70%, #8a5448 100%); }
  .hero-caption { left: 268px; top: 358px; width: 663px; height: 101px; background: rgba(28,24,28,.82);
    display: flex; align-items: center; justify-content: center; font-family: "Great Vibes", cursive; font-size: 62px; }
  .pink { color: var(--pink); }
  .dots { left: 562px; top: 661px; display: flex; gap: 13px; }
  .dots span { width: 8px; height: 8px; border-radius: 50%; background: var(--white); }
  .dots span.on { background: var(--pink); }

  .script-title { width: 1200px; left: 0; text-align: center; font-family: "Great Vibes", cursive; font-size: 56px; }

  /* products */
  .product { top: 926px; width: 218px; height: 298px; background: var(--panel); text-align: center; }
  .product-photo { position: absolute; left: 20px; top: 20px; width: 178px; height: 150px; border-radius: 6px; }
  .product-rule { position: absolute; left: 20px; right: 20px; top: 192px; border-top: 1px solid var(--panel-line); }
  .product-name { position: absolute; left: 0; right: 0; top: 226px; font-size: 16px; font-weight: 500; }
  .product-price { position: absolute; left: 0; right: 0; top: 258px; font-size: 16px; font-weight: 500; color: var(--pink); }
  .badge { position: absolute; top: 15px; padding: 2px 11px; font-size: 14px; font-weight: 500; color: var(--white); }
  .badge.new { left: 15px; background: var(--pink); }
  .badge.sale { right: 10px; background: var(--red-badge); }
  .badge.free { right: 10px; background: var(--pink); }

  .arrow { width: 46px; height: 46px; border: 1.5px solid #8a8a8c; border-radius: 50%; display: flex; align-items: center; justify-content: center; }

  /* membership */
  .membership { left: 144px; top: 1331px; width: 912px; height: 135px; background: var(--pink-soft); }
  .membership-title { left: 26px; top: 26px; font-family: "Great Vibes", cursive; font-size: 56px; }
  .membership-text { left: 451px; top: 40px; font-size: 19px; line-height: 28px; font-weight: 500; }
  .btn-white { left: 717px; top: 44px; width: 165px; height: 47px; background: var(--white); color: var(--ink);
    display: flex; align-items: center; justify-content: center; font-size: 19px; }

  /* categories */
  .categories-bg { left: 0; top: 1466px; width: 1200px; height: 680px;
    background: radial-gradient(ellipse at 50% 20%, #3f3c3e 0%, #262326 45%, var(--ink) 85%); }
  .category { top: 1697px; width: 290px; height: 255px; background: var(--grey-card); border: 2px solid #5a5a5c; }
  .category-photo { position: absolute; left: 0; top: 0; width: 100%; height: 201px; }
  .category-label { position: absolute; left: 0; right: 0; top: 222px; text-align: center; font-size: 16px; font-weight: 500; }
  .btn-pink { left: 479px; top: 2025px; width: 242px; height: 46px; background: var(--pink-soft);
    display: flex; align-items: center; justify-content: center; gap: 10px; font-size: 19px; font-weight: 500; }

  /* testimonial */
  .model-section { left: 0; top: 2192px; width: 1200px; height: 733px;
    background: linear-gradient(180deg, #232123 0%, #3a383a 50%, #1d1b1d 100%); }
  .model-photo { left: 260px; top: 2240px; width: 500px; height: 685px;
    background: radial-gradient(ellipse at 50% 40%, #8a8889 0%, #4c4a4c 55%, transparent 80%); }
  .quote-ring { left: 765px; top: 2361px; width: 402px; height: 402px; border-radius: 50%; background: var(--ring); }
  .quote-disc { left: 778px; top: 2374px; width: 376px; height: 376px; border-radius: 50%; background: var(--pink-soft); text-align: center; }
  .quote-text { position: absolute; left: 38px; right: 38px; top: 144px; font-style: italic; font-size: 15px; line-height: 23px; }
  .quote-name { position: absolute; left: 0; right: 0; top: 308px; font-size: 21px; font-weight: 600; }
  .quote-nav { left: 937px; top: 2727px; width: 58px; height: 58px; border-radius: 50%; background: var(--ring);
    display: flex; align-items: center; justify-content: center; }

  /* footer */
  .site-footer .brand { left: 0; width: 1200px; top: 3012px; justify-content: center; }
  .footer-nav { left: 144px; top: 3109px; width: 912px; height: 56px; border-top: 1px solid #2c2a2c; border-bottom: 1px solid #2c2a2c;
    display: flex; align-items: center; justify-content: center; gap: 26px; font-size: 16px; }
  .footer-nav span.sep { color: var(--muted); }
  .copyright { left: 0; width: 1200px; top: 3208px; text-align: center; font-size: 14px; }
  .social { left: 0; width: 1200px; top: 3260px; display: flex; justify-content: center; gap: 12px; }
  .social span { width: 36px; height: 36px; border-radius: 50%; background: var(--pink); }
</style>
</head>
<body>
<div class="page">

  <div class="abs side-photo left" role="img" aria-label="Black and white photo of a woman in lingerie"></div>
  <div class="abs side-photo right" role="img" aria-label="Black and white photo of a woman in lingerie"></div>

  <header class="site-header">
    <div class="abs brand"><span class="brand-dot"></span>Marisol Velvet</div>
    <nav class="abs main-nav">
      <a class="active" href="#">Home</a><a href="#">About</a><a href="#">Videos</a><a href="#">Membership</a><a href="#">Contact Us</a>
    </nav>
    <svg class="abs cart" width="44" height="34" viewBox="0 0 44 34" fill="none" stroke="#fb6ec0" stroke-width="3" stroke-linecap="round" stroke-linejoin="round">
      <path d="M2 4h7l5 18h22l5-14H12"/><circle cx="17" cy="29" r="2.5"/><circle cx="33" cy="29" r="2.5"/><path d="M22 10v8M18 14h8"/>
    </svg>
  </header>

  <section>
    <div class="abs hero" role="img" aria-label="Sunset over a rocky tropical coastline and sea"></div>
    <div class="abs hero-caption">Filmed in&nbsp;<span class="pink">Tropical</span>&nbsp;Locations</div>
    <div class="abs dots"><span></span><span class="on"></span><span></span></div>
  </section>

  <section>
    <h2 class="abs script-title" style="top:800px">Featured <span class="pink">Products</span></h2>
    <div class="abs arrow" style="left:71px;top:1052px"><svg width="14" height="20" viewBox="0 0 14 20" fill="none" stroke="#ccc" stroke-width="2"><path d="M10 2L3 10l7 8"/></svg></div>
    <div class="abs arrow" style="left:1083px;top:1052px"><svg width="14" height="20" viewBox="0 0 14 20" fill="none" stroke="#ccc" stroke-width="2"><path d="M4 2l7 8-7 8"/></svg></div>

    <article class="abs product" style="left:144px">
      <div class="product-photo" role="img" aria-label="Black lace lingerie set" style="background:radial-gradient(circle,#4a3a44,#1b1a1c 70%)"></div>
      <span class="badge new">NEW</span>
      <div class="product-rule"></div>
      <div class="product-name">PRODUCT NAME</div><div class="product-price">$56.98</div>
    </article>
    <article class="abs product" style="left:375px">
      <div class="product-photo" role="img" aria-label="Pink silicone toy" style="background:radial-gradient(circle,#e23fb0,#1b1a1c 65%)"></div>
      <div class="product-rule"></div>
      <div class="product-name">PRODUCT NAME</div><div class="product-price">$56.98</div>
    </article>
    <article class="abs product" style="left:607px">
      <div class="product-photo" role="img" aria-label="Purple glitter ring toy" style="background:radial-gradient(circle,#8a2ce0,#1b1a1c 65%)"></div>
      <span class="badge sale">SALE</span>
      <div class="product-rule"></div>
      <div class="product-name">PRODUCT NAME</div><div class="product-price">$56.98</div>
    </article>
    <article class="abs product" style="left:838px">
      <div class="product-photo" role="img" aria-label="Red high heels with handcuffs" style="background:radial-gradient(circle,#c0181c,#1b1a1c 65%)"></div>
      <div class="product-rule"></div>
      <div class="product-name">PRODUCT NAME</div><div class="product-price">$56.98</div>
    </article>
  </section>

  <section class="abs membership">
    <h2 class="abs membership-title">Monthly Membership</h2>
    <p class="abs membership-text">Lorem ipsum dolor sit<br>ectetipiscing elit</p>
    <a class="abs btn-white">VIEW PLAN</a>
  </section>

  <section>
    <div class="abs categories-bg" role="img" aria-label="Dim black and white photo of a couple in a masquerade mask"></div>
    <h2 class="abs script-title" style="top:1566px">Categories <span class="pink">For videos</span></h2>
    <div class="abs arrow" style="left:71px;top:1775px"><svg width="14" height="20" viewBox="0 0 14 20" fill="none" stroke="#ccc" stroke-width="2"><path d="M10 2L3 10l7 8"/></svg></div>
    <div class="abs arrow" style="left:1083px;top:1775px"><svg width="14" height="20" viewBox="0 0 14 20" fill="none" stroke="#ccc" stroke-width="2"><path d="M4 2l7 8-7 8"/></svg></div>

    <article class="abs category" style="left:141px">
      <div class="category-photo" role="img" aria-label="Outdoor lounge deck over a tropical sea" style="background:linear-gradient(180deg,#9fa6c8,#3a8ab8 55%,#4a3a34)"></div>
      <span class="badge free">FREE</span>
      <div class="category-label">OUTDOOR VIDEOS</div>
    </article>
    <article class="abs category" style="left:455px">
      <div class="category-photo" role="img" aria-label="Woman in a costume posing on a dark ornate bed" style="background:linear-gradient(180deg,#1c2a44,#22365c 60%,#151c2c)"></div>
      <div class="category-label">NAUGHTY COSTUMES</div>
    </article>
    <article class="abs category" style="left:769px">
      <div class="category-photo" role="img" aria-label="Legs in red high heels against a teal wall" style="background:linear-gradient(180deg,#7ec4c0,#5fa8a4 60%,#5a3424)"></div>
      <span class="badge free">FREE</span>
      <div class="category-label">SLUTTY WHORE-SHOES</div>
    </article>

    <a class="abs btn-pink">
      <svg width="20" height="20" viewBox="0 0 20 20" fill="#fff"><path d="M10 1l6 7h-4v6H8V8H4z"/><path d="M2 14h3v3h10v-3h3v5H2z"/></svg>
      UPLOAD VIDEOS
    </a>
  </section>

  <section>
    <div class="abs model-section"></div>
    <div class="abs model-photo" role="img" aria-label="Black and white photo of a woman in a lace bra holding handcuffs"></div>
    <div class="abs quote-ring"></div>
    <blockquote class="abs quote-disc">
      <svg style="position:absolute;left:148px;top:60px" width="80" height="56" viewBox="0 0 80 56" fill="none" stroke="#fff" stroke-width="3">
        <path d="M20 4a14 14 0 1 1 0 28c0 10-4 16-12 20M60 4a14 14 0 1 1 0 28c0 10-4 16-12 20"/>
      </svg>
      <p class="quote-text">Lorem ipsum dolor sit amet, consectetur adipiscing elit, sed do eiusmod tempor incididunt ut labore et dolore magna aliquauis ipsum suspendisse ultrices gravida. Risus commodo viverra maecenas accumsanfacilisis.</p>
      <p class="quote-name">- KALENA</p>
    </blockquote>
    <div class="abs quote-nav"><svg width="26" height="14" viewBox="0 0 26 14" fill="none" stroke="#fff" stroke-width="2"><path d="M8 2L3 7l5 5M18 2l5 5-5 5"/></svg></div>
  </section>

  <footer class="site-footer">
    <div class="abs brand"><span class="brand-dot"></span>Marisol Velvet</div>
    <nav class="abs footer-nav">
      <span>HOME</span><span class="sep">/</span><span>ABOUT</span><span class="sep">/</span><span>VIDEOS</span><span class="sep">/</span><span>MEMBERSHIP</span><span class="sep">/</span><span>CONTACT US</span>
    </nav>
    <p class="abs copyright">© 2020 Marisol Velvet . All Rights reserved &nbsp;|&nbsp; Privacy</p>
    <div class="abs social"><span></span><span></span><span></span></div>
  </footer>

</div>
</body>
</html>
```